ZEPRILO.COM is a premium domain sales company. Our competitors are companies like vastplots.example, getparcels.example, peerwords.example. Our current site is at www.zeprilos.example.

We want to have the ability to search for domains, to highlight special offers and have some testimonials on the index page.

The logo for the site is attached.

Please be sure that the order form fits on the screen without scrolling the page. I want the entire form, including the submit button to fit without any page scrolling.

Delivered product - INDEX PAGE, ORDER FORM AND CONTENT PAGE PSDs.

Target Market(s)

Small to Medium business professionals

Industry/Entity Type

It Company

Requirements
Must have
• 1. List of domains for sale
2. Simple search box with button to run the search
3. link for advanced search
4. testimonial area. Note - this can be a small box where a different testimonial is displayed on each page load.
Nice to have
• Would like the site to have some white space. Don't want a heavily packed website. Give it an "airy" feel.

```html
<!DOCTYPE html>
<html lang="en">
<head>
<meta charset="utf-8">
<title>ZEPRILO.COM — Premium Domains</title>
<link href="https://fonts.googleapis.com/css2?family=PT+Sans:ital,wght@0,400;0,700;1,400&family=Lora:ital@1&display=swap" rel="stylesheet">
<style>
:root{
  --green:#2f8a2a;
  --green-dark:#1f6a1c;
  --blue:#1f6eb8;
  --blue-deep:#1c4f86;
  --hero-a:#2a6fae;
  --hero-b:#184a7d;
  --navy:#1c3e6a;
  --dark:#333638;
  --darker:#262829;
  --sky:#1aa3e6;
  --orange:#f7a21b;
  --red:#d63a2c;
  --text:#555;
  --muted:#888;
  --line:#dcdcdc;
  --panel:#f2f2f2;
}
*{box-sizing:border-box;margin:0;padding:0}
html,body{width:779px;height:1200px;overflow:hidden;background:#fff}
body{font-family:"PT Sans",sans-serif;color:var(--text);position:relative;font-size:6px}
.abs{position:absolute}
.topbar{left:0;top:0;width:779px;height:16px;background:var(--green);color:#fff;font-size:5px;font-weight:700}
.topbar .welcome{left:121px;top:5px}
.topbar .links{right:129px;top:5px;display:flex;gap:14px}
.logo{font-weight:700;color:var(--navy);letter-spacing:-.5px;display:flex;align-items:center;gap:4px;white-space:nowrap}
.logo .dot{width:10px;height:10px;border-radius:50%;background:var(--green)}
.header-logo{left:118px;top:34px;font-size:21px}
.keyword{left:398px;top:37px;width:118px;height:12px;border:1px solid #ccc;font-size:4.5px;color:#999;padding:3px 5px}
.questions{left:526px;top:23px;width:135px;height:41px;border:1px solid #ddd;padding:5px 8px}
.questions b{display:block;color:var(--navy);font-size:9px;font-weight:400}
.questions small{display:block;font-size:4px;color:#444;font-weight:700}
.questions span{display:block;color:var(--blue);font-size:7.5px;margin-top:2px}
.questions .agent{right:3px;top:3px;width:32px;height:34px;background:linear-gradient(#e8d8cf,#b9a39a);border-radius:2px}
.nav{left:117px;top:72px;width:545px;height:22px;background:linear-gradient(#4a4d4f,var(--darker));display:flex;font-size:6px;color:#fff}
.nav a{color:#fff;text-decoration:none;line-height:22px;padding:0 14px}
.nav a.on{background:var(--blue);padding:0 17px}
.nav .fill{flex:1;display:flex;justify-content:space-around}
.hero{left:0;top:94px;width:779px;height:256px;background:radial-gradient(ellipse at 60% 40%,var(--hero-a),var(--hero-b))}
.hero h1{left:121px;top:68px;color:#fff;font-weight:400;font-size:19px}
.hero h2{left:121px;top:95px;color:#fff;font-weight:400;font-size:13px}
.arrow{top:106px;font-size:30px;color:rgba(255,255,255,.25)}
.tab{left:123px;top:125px;width:111px;height:25px;background:#e6e6e6;color:#444;font-size:8px;padding:8px 10px}
.domainbox{left:123px;top:150px;width:301px;height:23px;background:#fff;font-size:7.5px;color:#aaa}
.domainbox .ph{left:10px;top:7px}
.domainbox .ext{left:198px;top:7px;color:#666}
.btn-search{left:236px;top:3px;width:62px;height:17px;background:linear-gradient(#45a33e,var(--green-dark));color:#fff;text-align:center;line-height:17px;font-size:7.5px}
.hero .links{left:125px;top:183px;color:#fff;font-size:5px;font-weight:700;display:flex;gap:12px}
.hero .photo{left:432px;top:2px;width:192px;height:240px;background:radial-gradient(ellipse at 50% 55%,#6e6b74,#2d5b8c 70%);border-radius:40% 40% 10% 10%}
.adv{left:0;top:350px;width:779px;height:41px;background:var(--dark)}
.adv .label{left:117px;top:0;width:115px;height:41px;background:linear-gradient(#3f9a38,var(--green-dark));color:#fff;font-size:9.5px;padding:9px 0 0 17px;line-height:12px}
.adv .lens{left:196px;top:-8px}
.field-l{color:#ccc;font-size:4.5px;top:8px}
.fbox{top:20px;height:12px;background:#4a4d4f;border:1px solid #555}
.checks{left:359px;top:21px;color:#ccc;font-size:5px;display:flex;gap:5px;align-items:center}
.checks i{display:inline-block;width:6px;height:6px;background:#eee;margin-right:2px;vertical-align:middle}
.to{top:22px;color:#ccc;font-size:5px}
.find{left:566px;top:387px;width:96px;height:27px;background:var(--darker);padding:3px}
.find div{background:linear-gradient(#2d95e0,var(--blue));color:#fff;font-size:9px;text-align:center;line-height:19px;height:19px}
.welcome-h{left:0;width:779px;top:408px;display:flex;justify-content:center;align-items:center;gap:6px}
.welcome-h em{font-family:"Lora",serif;font-size:16px;color:#666}
.welcome-h .logo{font-size:21px}
.intro{left:122px;top:446px;width:535px;text-align:center;font-size:5.3px;line-height:9.5px}
.news{left:117px;top:477px;width:545px;height:47px;background:var(--panel)}
.news h3{left:13px;top:8px;color:var(--navy);font-weight:400;font-size:8px}
.news p{left:13px;top:21px;width:440px;font-size:5px;color:#888;line-height:9.5px}
.news .more{left:454px;top:9px;width:80px;height:26px;background:linear-gradient(#999,#6b6b6b);color:#fff;font-size:8px;text-align:center;line-height:26px;border:1px solid #555}
.tabs{left:117px;top:539px;display:flex;gap:2px}
.tabs div{height:20px;padding:0 10px;line-height:20px;font-size:5.8px;background:linear-gradient(#777,#5a5a5a);color:#fff}
.tabs .on{background:var(--blue);width:85px}
.listing{left:117px;top:558px;width:375px;height:165px;border:1px solid var(--line)}
.listing .hd{position:absolute;top:9px;height:13px;background:#bfbfbf;color:#fff;font-size:4.8px;text-align:center;line-height:13px}
.rows{left:9px;top:31px;width:356px}
.row{height:16px;display:flex;align-items:center;font-size:5px;color:#444;border-bottom:1px solid #fff}
.row:nth-child(odd){background:#ececec}
.row span:nth-child(1){width:121px;padding-left:10px}
.row span:nth-child(2){width:88px}
.row span:nth-child(3){width:90px}
.row span:nth-child(4){display:flex;align-items:center;gap:4px}
.go{width:8px;height:8px;border-radius:50%;background:var(--red);display:inline-block}
.testi-h{left:513px;top:543px;color:var(--navy);font-size:9.5px;font-weight:400}
.testi{left:509px;top:558px;width:153px;height:165px;background:linear-gradient(#f3f3f3,#fff)}
.testi .q{font-family:"Lora",serif;font-size:20px;color:#ccc}
.testi h4{left:23px;top:25px;color:var(--green);font-size:5.5px;font-weight:700}
.testi .pic{left:22px;top:42px;width:55px;height:58px;background:linear-gradient(#4a8fc9,#c89a7a);border:2px solid #fff;box-shadow:0 0 1px #999}
.testi .side{left:91px;top:42px;width:58px;font-size:5px;line-height:10px;color:#888}
.testi .low{left:23px;top:106px;width:120px;font-size:5px;line-height:10px;color:#888}
.testi .by{left:23px;top:143px;font-size:5px;color:var(--green);font-style:italic;line-height:10px}
.value-h{left:0;width:779px;text-align:center;top:737px;color:var(--navy);font-size:9.5px;font-weight:400}
.card{top:758px;width:129px;height:47px;border:1px solid var(--line);background:linear-gradient(#fff,#f4f4f4)}
.card .ic{left:7px;top:10px;width:30px;height:28px}
.card h5{left:43px;top:10px;color:var(--navy);font-size:7px;font-weight:400}
.card p{left:43px;top:21px;width:82px;font-size:5px;line-height:10px;color:#555}
.promo{left:117px;top:824px;width:545px;height:218px;background:radial-gradient(circle at 92% 8%,#e9f8ff 0,#6cc8f3 18%,var(--sky) 45%,#1277c4 100%)}
.promo .photo{left:35px;top:5px;width:200px;height:213px;background:linear-gradient(160deg,#f2d9a3,#9dd8f0 60%,#3da0d8);border-radius:45% 45% 0 0}
.promo .make{left:263px;top:28px;color:#fff;font-size:26px}
.promo .your{left:263px;top:50px;color:#fff;font-size:37px}
.promo p{left:266px;width:260px;color:#fff;font-size:6.3px;line-height:10.5px}
.promo .cta{left:268px;top:161px;width:159px;height:25px;background:linear-gradient(#ffbb2e,#f08d0e);color:#fff;font-size:7px;text-align:center;line-height:25px;border:1px solid #d77f08}
.foot{left:117px;top:1057px;width:545px;height:96px;background:linear-gradient(#eee,#fff);border-top:1px solid #ddd}
.col{top:13px}
.col h6{color:var(--navy);font-size:6.5px;font-weight:400;margin-bottom:5px}
.col li{list-style:none;font-size:4.6px;color:#555;line-height:10.5px}
.bottom{left:117px;top:1155px;width:545px;height:45px;border-top:1px solid #ddd}
.bottom .logo{left:1px;top:12px;font-size:13px}
.bottom .copy{left:96px;top:18px;font-size:4.3px;white-space:nowrap}
.pay{left:228px;top:9px;width:130px;height:24px;border:1px solid #ccc;border-radius:3px;display:flex;align-items:center;gap:4px;padding:0 6px}
.pay i{display:block;height:12px;background:#d9d9d9}
.follow{left:414px;top:16px;display:flex;align-items:center;gap:4px;font-size:5.5px;color:#555}
.follow i{display:block;width:14px;height:14px;border-radius:3px;background:var(--blue-deep)}
.follow i:last-child{background:var(--orange)}
</style>
</head>
<body>

<div class="abs topbar">
  <span class="abs welcome">WELCOME TO GUEST</span>
  <div class="abs links"><span>LOGIN</span><span>MY ACCOUNT</span><span>YOUR CART IS : 0 ITEMS</span></div>
</div>

<div class="abs logo header-logo"><span class="dot"></span>ZEPRILO.COM</div>
<div class="abs keyword">ENTER YOUR KEYWORD :</div>
<div class="abs questions">
  <b>QUESTIONS?</b><small>WE'RE HERE TO HELP! CALL TODAY!</small><span>(2020) 555 014</span>
  <div class="abs agent" role="img" aria-label="Support agent wearing a headset"></div>
</div>

<nav class="abs nav">
  <a class="on">HOME</a>
  <div class="fill"><a>DELETING DOMAINS</a><a>DOMAINS FOR SALE</a><a>TESTIMONIALS</a><a>NEWS</a><a>FAQ'S</a><a>SUPPORT</a></div>
</nav>

<section class="abs hero">
  <h1 class="abs">OUR BUSINESS STARTS HERE</h1>
  <h2 class="abs">BUY A PREMIUM DOMAIN AND OPEN YOUR DOORS</h2>
  <span class="abs arrow" style="left:82px">&#10094;</span>
  <span class="abs arrow" style="left:673px">&#10095;</span>
  <div class="abs tab">SEARCH FOR A DOMAIN</div>
  <div class="abs domainbox">
    <span class="abs ph">ENTER DOMAIN NAME</span>
    <span class="abs ext">.COM &#8964;</span>
    <div class="abs btn-search">SEARCH</div>
  </div>
  <div class="abs links"><span>BULK SEARCH</span><span>|</span><span>ALL DOMAIN PRICING</span><span>|</span><span>RISK-FREE DOMAIN TRANSFERS</span></div>
  <div class="abs photo" role="img" aria-label="Smiling woman sitting cross-legged with a laptop, giving a thumbs up"></div>
</section>

<section class="abs adv">
  <div class="abs label">ADVANCED<br>&nbsp;&nbsp;&nbsp;SEARCH</div>
  <svg class="abs lens" width="40" height="50" viewBox="0 0 40 50"><circle cx="22" cy="16" r="13" fill="rgba(255,255,255,.25)" stroke="#ddd" stroke-width="3"/><line x1="13" y1="26" x2="2" y2="44" stroke="#777" stroke-width="5" stroke-linecap="round"/></svg>
  <span class="abs field-l" style="left:247px">KEYWORD(S):</span>
  <div class="abs fbox" style="left:247px;width:102px"></div>
  <span class="abs field-l" style="left:359px">EXTENSION:</span>
  <div class="abs checks"><span><i></i>ALL</span><span><i></i>.com</span><span><i></i>.net</span><span><i></i>.org</span></div>
  <span class="abs field-l" style="left:481px">PRICE:</span>
  <div class="abs fbox" style="left:481px;width:35px"></div><span class="abs to" style="left:520px">to</span>
  <div class="abs fbox" style="left:529px;width:35px"></div>
  <span class="abs field-l" style="left:578px">LENGTH:</span>
  <div class="abs fbox" style="left:578px;width:35px"></div><span class="abs to" style="left:617px">to</span>
  <div class="abs fbox" style="left:627px;width:35px"></div>
</section>
<div class="abs find"><div>FIND DOMAIN</div></div>

<div class="abs welcome-h"><em>Welcome to</em><span class="logo"><span class="dot"></span>ZEPRILO.COM</span></div>
<p class="abs intro">Lorem Ipsum is simply dummy text of the printing and typesetting industry. Lorem Ipsum has been the industry's standard dummy text ever since the 1500s, when an unknown printer took a galley of type and scrambled it to make a type specimen book. It has survived not only five centuries, but also the leap into electronic typesetting, remaining essentially unchanged.</p>

<section class="abs news">
  <h3 class="abs">LATEST NEWS</h3>
  <p class="abs">Lorem Ipsum is simply dummy text of the printing and typesetting industry. Lorem Ipsum has been the industry's standard dummy text ever since the 1500s, when an unknown printer. when an unknown printer.</p>
  <div class="abs more">VIEW MORE</div>
</section>

<div class="abs tabs"><div class="on">FEATURED DOMAIN</div><div>DOMAIN CATEGORIES</div><div>DAILY DOMAIN DEALS</div></div>
<section class="abs listing">
  <div class="hd" style="left:10px;width:46px">DOMAIN</div>
  <div class="hd" style="left:141px;width:46px">CATEGORY</div>
  <div class="hd" style="left:226px;width:46px">PRICE</div>
  <div class="hd" style="left:314px;width:46px">OPTION</div>
  <div class="abs rows">
    <div class="row"><span>QuillmereArt.example</span><span>Gift</span><span>&#9906; $6,095</span><span>Buy now <i class="go"></i></span></div>
    <div class="row"><span>QuillmereArt.example</span><span>Gift</span><span>&#9906; $6,095</span><span>Buy now <i class="go"></i></span></div>
    <div class="row"><span>QuillmereArt.example</span><span>Gift</span><span>&#9906; $6,095</span><span>Buy now <i class="go"></i></span></div>
    <div class="row"><span>QuillmereArt.example</span><span>Gift</span><span>&#9906; $6,095</span><span>Buy now <i class="go"></i></span></div>
    <div class="row"><span>QuillmereArt.example</span><span>Gift</span><span>&#9906; $6,095</span><span>Buy now <i class="go"></i></span></div>
    <div class="row"><span>QuillmereArt.example</span><span>Gift</span><span>&#9906; $6,095</span><span>Buy now <i class="go"></i></span></div>
    <div class="row"><span>QuillmereArt.example</span><span>Gift</span><span>&#9906; $6,095</span><span>Buy now <i class="go"></i></span></div>
    <div class="row"><span>QuillmereArt.example</span><span>Gift</span><span>&#9906; $6,095</span><span>Buy now <i class="go"></i></span></div>
  </div>
</section>

<h3 class="abs testi-h">TESTIMONIALS</h3>
<section class="abs testi">
  <span class="abs q" style="left:10px;top:0">&ldquo;</span>
  <h4 class="abs">RENEWAL FACILITIES FOR DOMAIN</h4>
  <div class="abs pic" role="img" aria-label="Portrait of the client giving the testimonial"></div>
  <p class="abs side">Lorem Ipsum is simply dummy text of the printing and typesetting industry. Lorem Ipsum has been the</p>
  <p class="abs low">Lorem Ipsum is simply dummy text of the printing and typesetting industry. Lorem Ip sum has been the industry's.</p>
  <p class="abs by">Loren Vask<br>posted on 20 may 2013</p>
  <span class="abs q" style="left:131px;top:128px">&rdquo;</span>
</section>

<h3 class="abs value-h">THE VALUE OF DOMAINS</h3>
<div class="abs card" style="left:117px">
  <svg class="abs ic" viewBox="0 0 30 28"><rect x="3" y="9" width="24" height="16" rx="2" fill="#ddd" stroke="#999"/><path d="M15 14 L15 2 A12 12 0 0 1 26 10 Z" fill="#e23b2e"/><path d="M15 14 L26 10 A12 12 0 0 1 20 24 Z" fill="#3d8be0"/><path d="M15 14 L20 24 A12 12 0 0 1 4 10 Z" fill="#f2c12e"/><path d="M15 14 L4 10 A12 12 0 0 1 15 2 Z" fill="#4cae3c"/></svg>
  <h5 class="abs">DOMAIN VALUATIONS</h5><p class="abs">Lorem Ipsum is simply dummy text of the printing.</p>
</div>
<div class="abs card" style="left:255px">
  <svg class="abs ic" viewBox="0 0 30 28"><path d="M15 3 L28 25 L2 25 Z" fill="#f5c518" stroke="#c99a00"/><rect x="14" y="10" width="2.4" height="9" fill="#222"/><rect x="14" y="20.5" width="2.4" height="2.4" fill="#222"/></svg>
  <h5 class="abs">DOMAINS 101</h5><p class="abs">Lorem Ipsum is simply dummy text of the printing.</p>
</div>
<div class="abs card" style="left:394px">
  <svg class="abs ic" viewBox="0 0 30 28"><ellipse cx="15" cy="17" rx="14" ry="8" fill="#7cc242"/><path d="M15 15 L15 5 A14 9 0 0 1 29 14 Z" fill="#f2c12e"/></svg>
  <h5 class="abs">BUSINESS ASSETS</h5><p class="abs">Lorem Ipsum is simply dummy text of the printing.</p>
</div>
<div class="abs card" style="left:533px">
  <svg class="abs ic" viewBox="0 0 30 28"><circle cx="15" cy="14" r="12" fill="#e84b3a"/><circle cx="15" cy="14" r="6" fill="#fff"/><path d="M7 6 L11 10 M23 6 L19 10 M7 22 L11 18 M23 22 L19 18" stroke="#fff" stroke-width="5"/></svg>
  <h5 class="abs">AVOIDING PROBLEMS</h5><p class="abs">Lorem Ipsum is simply dummy text of the printing.</p>
</div>

<section class="abs promo">
  <div class="abs photo" role="img" aria-label="Smiling woman holding a card reading that the domain is easy to buy"></div>
  <span class="abs make">Make it</span>
  <span class="abs your">Your Domain</span>
  <p class="abs" style="top:100px">Your website is the face of your business. Choosing a Premium Domain will give you instant recognition with your customers.</p>
  <p class="abs" style="top:131px">Our domain experts help thousands of businesses each month select the right domain name. Let us connect you with the best domain for your needs.</p>
  <div class="abs cta">CLICK HERE FOR VIEW MORE DETRAILS</div>
</section>

<footer class="abs foot">
  <div class="abs col" style="left:13px"><h6>ACCOUNT INFORMATION</h6><ul><li>MY DASHBOARD</li><li>MY PROFILE</li><li>MY SERVICES &amp; RENEWALS</li><li>ORDER HISTORY</li></ul></div>
  <div class="abs col" style="left:136px"><h6>PRODUCT &amp; SERVICES</h6><ul><li>DOMAIN REGISTRATION</li><li>WEB HOSTING</li><li>EMAIL HOSTING</li><li>CLOUD SERVER</li><li>EASY SITE/WEBSITE BUILDER</li><li>SSL</li></ul></div>
  <div class="abs col" style="left:253px"><h6>DELETING DOMAINS</h6><ul><li>TRAFFIC SCORE</li><li>DOMAIN RANK</li><li>POPULARITY SCORE</li><li>US BASED TRAFFIC PERCENT</li></ul></div>
  <div class="abs col" style="left:370px"><h6>DOMAINS FOR SALE</h6><ul><li>NEWEST DOMAINS</li><li>ELITE DOMAINS</li><li>CHEAP DOMAINS</li></ul></div>
  <div class="abs col" style="left:475px"><h6>FAQ</h6><ul><li>BACKORDER FAQ</li><li>OFFER FAQ</li><li>PURCHASE FAQ</li></ul></div>
</footer>

<div class="abs bottom">
  <div class="abs logo">ZEPRILO.COM</div>
  <span class="abs copy">COPYRIGHT © 2013 ZEPRILO. ALL RIGHTS RESERVED.</span>
  <div class="abs pay" aria-label="Accepted payment methods">
    <i style="width:16px;height:16px;border-radius:50%;background:#f3d36b"></i>
    <i style="width:36px"></i><i style="width:14px"></i><i style="width:14px"></i><i style="width:14px"></i><i style="width:14px"></i>
  </div>
  <div class="abs follow" aria-label="Social links">FOLLOW US : <i></i><i></i><i></i><i></i><i></i></div>
</div>

</body>
</html>
```